Dialysis Brochure

12 pages booklet, horizontal, 9 inches width x 6 inches high , luxury look
Updates

Landscape booklet 9 x 6

Need extra days to review

Target Market(s)

General public

Industry/Entity Type

Health Care

Colors

Designer to choose colors to be used in the design.

Requirements
Nice to have
• foil effect or similar

```html
<!DOCTYPE html>
<html lang="en">
<head>
<meta charset="utf-8">
<title>Dialysis Brochure – Inside Spread</title>
<link href="https://fonts.googleapis.com/css2?family=Roboto:wght@400;700&display=swap" rel="stylesheet">
<style>
  :root{
    --canvas:#e9e6e1;
    --page-dark:#55585c;
    --page-mid:#6e7175;
    --page-light:#8a8d91;
    --ink:#f2f3f4;
    --ink-soft:#dadcde;
    --blue:#1f8fb8;
    --blue-deep:#0f6f98;
    --blue-light:#4fb4d8;
    --photo-a:#c9cdd1;
    --photo-b:#8e969e;
  }
  html,body{margin:0;padding:0;width:1200px;height:901px;overflow:hidden;background:var(--canvas);}
  .spread{
    position:absolute;left:30px;top:260px;width:1140px;height:380px;
    box-shadow:0 14px 30px rgba(0,0,0,.25);
    font-family:"Roboto",Arial,sans-serif;color:var(--ink);
  }
  .page{position:absolute;top:0;width:570px;height:380px;overflow:hidden;}
  .page--left{left:0;background:linear-gradient(160deg,var(--page-light) 0%,var(--page-mid) 40%,var(--page-dark) 100%);}
  .page--right{left:570px;background:linear-gradient(200deg,var(--page-light) 0%,var(--page-mid) 45%,var(--page-dark) 100%);}
  .page-backdrop{position:absolute;inset:0;opacity:.35;background:linear-gradient(90deg,rgba(255,255,255,.15),rgba(0,0,0,.1));}
  .photo{position:absolute;background:linear-gradient(160deg,var(--photo-a),var(--photo-b));}
  .photo--clinic-floor{left:300px;top:40px;width:220px;height:305px;}
  .photo--treatment-room{left:80px;top:35px;width:220px;height:305px;}
  .chevrons{position:absolute;left:0;top:0;width:1140px;height:380px;}
  .section{position:absolute;font-size:10.5px;line-height:1.35;}
  .section h2{font-size:11.5px;font-weight:700;margin:0 0 12px;letter-spacing:.2px;text-transform:uppercase;}
  .section p{margin:0 0 12px;color:var(--ink-soft);}
  .section ul{margin:0;padding-left:14px;color:var(--ink-soft);}
  .section li{margin-bottom:4px;}
  .section--transplant{left:50px;top:90px;width:235px;}
  .section--transplant li{margin-bottom:6px;}
  .section--social{left:880px;top:60px;width:235px;}
  .brand{position:absolute;display:flex;align-items:center;gap:5px;
    font-family:"Roboto",Arial,sans-serif;font-weight:700;font-size:8.5px;line-height:1.15;color:var(--ink);text-transform:uppercase;letter-spacing:.4px;}
  .brand-dot{width:10px;height:10px;border-radius:50%;background:var(--ink);flex:none;}
  .brand--left{left:508px;top:120px;width:58px;}
  .brand--right{left:590px;top:205px;width:80px;}
</style>
</head>
<body>
  <div class="spread">
    <div class="page page--left">
      <div class="page-backdrop" role="img" aria-label="Faded photograph of a dialysis treatment hall"></div>
      <div class="photo photo--clinic-floor" role="img" aria-label="Photograph of a bright dialysis floor with a nurse talking to a seated patient"></div>
    </div>
    <div class="page page--right">
      <div class="page-backdrop" role="img" aria-label="Faded photograph of a clinic corridor with glass doors"></div>
      <div class="photo photo--treatment-room" role="img" aria-label="Photograph of a private treatment room with a grey recliner chair"></div>
    </div>

    <svg class="chevrons" viewBox="0 0 1140 380" aria-hidden="true">
      <defs>
        <linearGradient id="blueFoil" x1="0" y1="0" x2="1" y2="1">
          <stop offset="0" stop-color="var(--blue-light)"/>
          <stop offset=".5" stop-color="var(--blue)"/>
          <stop offset="1" stop-color="var(--blue-deep)"/>
        </linearGradient>
      </defs>
      <polygon points="535,0 570,0 570,380 560,380 500,190" fill="url(#blueFoil)"/>
      <polyline points="535,0 500,190 560,380" fill="none" stroke="#ffffff" stroke-opacity=".8" stroke-width="2"/>
      <polygon points="570,0 620,0 690,190 625,380 570,380" fill="url(#blueFoil)"/>
      <polyline points="620,0 690,190 625,380" fill="none" stroke="#ffffff" stroke-opacity=".8" stroke-width="2"/>
      <line x1="570" y1="0" x2="570" y2="380" stroke="#000" stroke-opacity=".2" stroke-width="1"/>
    </svg>

    <div class="brand brand--left"><span class="brand-dot"></span><span>Harborline Kidney Care</span></div>
    <div class="brand brand--right"><span class="brand-dot"></span><span>Harborline Kidney Care</span></div>

    <section class="section section--transplant">
      <h2>Kidney Transplant Program</h2>
      <p>Every patients of HKC who is interested in kidney transplant will be evaluated by Transplant Center Team Specialists.</p>
      <p>Harborline Kidney Care is affiliated with the following UNIVERSITY HOSPITAL TRANSPLANT PROGRAMS:</p>
      <ul>
        <li>Eastbridge Presbyterian / Ridgemont University Medical Center</li>
        <li>EBP / Halvorsen Medical Center</li>
        <li>Ashgrove University Medical Center</li>
        <li>Mount Calder Medical Center</li>
        <li>Westhaven Medical Center / Corwin College of Medicine</li>
      </ul>
    </section>

    <section class="section section--social">
      <h2>Social Worker Services</h2>
      <ul>
        <li>Assisting with keeping or obtaining insurance coverage</li>
        <li>Locate and access community resources</li>
        <li>Apply and obtain financial assistance, Medicaid</li>
        <li>Arrange transportation</li>
        <li>Home care services</li>
        <li>Physical, Occupational, and Speech Therapies</li>
        <li>Coordinate dialysis and work schedule, Vocational Rehabilitation</li>
        <li>Arrange Dialysis while you travel</li>
        <li>Psychosocial counseling to patients and family</li>
      </ul>
    </section>
  </div>
</body>
</html>
```